The Marrowvale

We need a APP for our members. this is a Private Bar/Venue. history of the brick building is it was built in1898 and was a gentleman club, oyster house, cigar factory and then law offices before we purchased and are beginning restoration.
the APP must include
1. direct texting to the concierge
2. calendar of events
3. veltrin Lock To open the lock, anyone with a code can approach the door, enable their phone's Bluetooth and press the relevant address from the app.
Read more: http://www.brevortgazette.co.uk/gadgetry/article-5182640/no-more-keys-phone-unlocks-your-front-door-from-anywhere.html#qwx8bRT2mkZp
4. Menus from various restaurants from our surrounding area
5. member name and member number to give the feel that the app is personalized
6. the members account balance
7. ability to pay their bill with credit card or zim tally monthly and automatically.
8. link to quöla with its own icon within the app.
9.the ability to reserve the room
Anything else that may of interest for our members that may be relevant that I may not have mentioned since we are new at this...
35 to 60 years of age
Club

```html
<!DOCTYPE html>
<html lang="en">
<head>
<meta charset="utf-8">
<title>The Marrowvale – Member App Screens</title>
<link href="https://fonts.googleapis.com/css2?family=ABeeZee:ital@0;1&display=swap" rel="stylesheet">
<style>
  :root{
    --page:#ffffff;
    --screen:#3b3b3b;
    --ink:#ffffff;
    --ink-soft:#d6d6d6;
    --hint:#b9b9b9;
    --pill:#0aa0e6;
    --button:#ececec;
    --button-ink:#222222;
    --alert:#ff0000;
    --badge:#1f5fe0;
    --status:#f3f000;
    --rule:#6fa3c7;
    --card:rgba(255,255,255,0.13);
    --caption:#222222;
  }
  *{box-sizing:border-box;margin:0;padding:0}
  html,body{width:1200px;height:1000px;overflow:hidden;background:var(--page)}
  body{position:relative;font-family:"ABeeZee",sans-serif;color:var(--ink)}

  .screen{position:absolute;top:153px;width:390px;height:695px;overflow:hidden;background:var(--screen)}
  .screen--login{left:158px}
  .screen--welcome{left:653px}
  .caption{position:absolute;top:868px;font-size:20px;line-height:25px;color:var(--caption)}
  .caption--login{left:38px}
  .caption--welcome{left:1094px}

  .backdrop{position:absolute;inset:0;background:linear-gradient(180deg,#5d5f60 0%,#4a4b4b 25%,#3a3a3a 55%,#343434 100%)}
  .avatar{position:absolute;width:110px;height:110px;border-radius:50%;
    background:radial-gradient(circle at 50% 40%,#c9a48a 0%,#a88a72 45%,#d9d3c6 100%)}

  /* login */
  .masthead{position:absolute;left:0;top:0;width:390px;height:186px;
    background:linear-gradient(180deg,#6b6f70,#505353 70%,#454545)}
  .masthead::after{content:"";position:absolute;left:0;bottom:0;width:100%;height:3px;background:var(--ink)}
  .club-name{position:absolute;top:76px;left:0;width:390px;text-align:center;font-size:26px;line-height:32px;color:var(--ink)}
  .field{position:absolute;left:54px;width:282px;border-bottom:2px solid var(--ink);
    font-style:italic;font-size:19px;color:var(--hint);padding-bottom:2px}
  .btn{position:absolute;border-radius:24px;background:var(--button);color:var(--button-ink);text-align:center;font-size:21px}
  .btn--login{left:100px;top:531px;width:190px;height:46px;line-height:46px}
  .btn--signup{left:100px;top:595px;width:190px;height:46px;line-height:46px}

  /* welcome */
  .member-name{position:absolute;top:140px;left:0;width:390px;text-align:center;font-size:20px}
  .dot{display:inline-block;width:8px;height:8px;border-radius:50%;background:var(--status);vertical-align:middle;margin-left:5px}
  .tag{position:absolute;left:26px;height:21px;line-height:21px;padding:0 7px;border-radius:10px;background:var(--pill);font-size:14px}
  .bio{position:absolute;left:26px;top:223px;width:336px;font-size:12.4px;line-height:14.6px;color:var(--ink)}
  .phone-row{position:absolute;left:70px;font-style:italic;font-size:11px}
  .phone-row span{position:absolute;left:46px;top:10px;width:184px;border-bottom:2px solid var(--rule)}
  .chat{position:absolute;left:33px;width:324px;height:56px;border-radius:22px;background:var(--card)}
  .chat .avatar{width:50px;height:50px;left:3px;top:3px;background:radial-gradient(circle,#8a8a8a,#2d2d2d)}
  .chat-name{position:absolute;left:60px;top:3px;font-size:11px}
  .chat-text{position:absolute;left:58px;top:24px;width:258px;font-style:italic;font-size:11px;line-height:13px;color:var(--ink-soft)}
  .scroll-track{position:absolute;left:368px;top:465px;width:8px;height:112px;border-radius:4px;background:var(--ink)}
  .scroll-thumb{position:absolute;left:0;top:0;width:8px;height:38px;border-radius:4px;background:#ff4040}
  .btn--logout{left:142px;top:594px;width:112px;height:33px;line-height:33px;font-size:16px;border-radius:17px}
  .toolbar{position:absolute;left:4px;top:637px;width:381px;height:48px;border-radius:14px;background:var(--alert);display:flex}
  .tool{flex:1;display:flex;align-items:center;justify-content:center;position:relative}
  .tool + .tool::before{content:"";position:absolute;left:0;top:6px;height:36px;border-left:2px solid var(--ink)}
  .badge{position:absolute;right:16px;top:3px;width:14px;height:14px;border-radius:50%;background:var(--badge);font-size:10px;line-height:14px;text-align:center}
</style>
</head>
<body>

<section class="screen screen--login">
  <div class="backdrop" role="img" aria-label="Blurred photo of a boardroom with a long table and chairs"></div>
  <header class="masthead" role="img" aria-label="Photo of a boardroom with windows behind">
    <div class="club-name">The Marrowvale</div>
  </header>
  <div class="avatar" style="left:141px;top:225px" role="img" aria-label="Member profile photo"></div>
  <div class="field" style="top:370px">Name</div>
  <div class="field" style="top:440px">Phone No.</div>
  <div class="btn btn--login">LOGIN</div>
  <div class="btn btn--signup">SIGN UP</div>
</section>

<section class="screen screen--welcome">
  <div class="backdrop" role="img" aria-label="Faint blurred photo of a boardroom"></div>
  <div class="avatar" style="left:139px;top:20px" role="img" aria-label="Member profile photo"></div>
  <div class="member-name">Elias Thorne<span class="dot"></span></div>

  <div class="tag" style="top:185px">Bio</div>
  <p class="bio">Lorem ipsum dolor sit amet, consectetur adipiscing elit, sed do eiusmod tempor incididunt ut labore et dolore magna aliqua. Ut enim ad minim veniam, quis nostrud exercitation.</p>

  <div class="tag" style="top:310px">Phone No.</div>
  <div class="phone-row" style="top:355px">OFFICE :<span></span></div>
  <div class="phone-row" style="top:383px;left:73px">HOME :<span style="left:43px"></span></div>

  <div class="tag" style="top:429px;font-size:12.5px">Recent Chats</div>
  <div class="chat" style="top:461px">
    <div class="avatar" role="img" aria-label="Contact profile photo"></div>
    <div class="chat-name">Corbin<span class="dot" style="width:7px;height:7px"></span></div>
    <div class="chat-text">Hi mate! What is all about the new meeting?</div>
  </div>
  <div class="chat" style="top:524px">
    <div class="avatar" role="img" aria-label="Contact profile photo"></div>
    <div class="chat-name">Wesley H<span class="dot" style="width:7px;height:7px"></span></div>
    <div class="chat-text" style="top:23px">How are we going to plan our next drive to the new hotel in the east?</div>
  </div>
  <div class="scroll-track"><div class="scroll-thumb"></div></div>

  <div class="btn btn--logout">LOG OUT</div>

  <nav class="toolbar">
    <div class="tool" aria-label="Messages">
      <svg width="30" height="22" viewBox="0 0 30 22"><rect x="1" y="1" width="28" height="20" fill="#fff"/><path d="M1 1 L15 12 L29 1 M1 21 L11 10 M29 21 L19 10" stroke="#ff0000" stroke-width="2" fill="none"/></svg>
    </div>
    <div class="tool" aria-label="Payments">
      <svg width="34" height="30" viewBox="0 0 34 30"><rect x="2" y="4" width="26" height="16" rx="2" fill="#fff" transform="rotate(-10 15 12)"/><rect x="5" y="12" width="26" height="14" rx="2" fill="#fff" stroke="#ff0000" stroke-width="1.5"/><rect x="5" y="15" width="26" height="3" fill="#ff0000"/><circle cx="24" cy="24" r="6" fill="#fff" stroke="#ff0000" stroke-width="1.5"/><text x="24" y="27.5" font-size="9" text-anchor="middle" fill="#ff0000" font-family="ABeeZee,sans-serif">$</text></svg>
    </div>
    <div class="tool" aria-label="Events calendar">
      <svg width="28" height="28" viewBox="0 0 28 28"><rect x="1" y="3" width="26" height="24" rx="2" fill="#fff"/><rect x="6" y="0" width="3" height="6" fill="#fff"/><rect x="19" y="0" width="3" height="6" fill="#fff"/><g fill="#ff0000"><rect x="4" y="11" width="4" height="3"/><rect x="10" y="11" width="4" height="3"/><rect x="16" y="11" width="4" height="3"/><rect x="22" y="11" width="3" height="3"/><rect x="4" y="16" width="4" height="3"/><rect x="10" y="16" width="4" height="3"/><rect x="16" y="16" width="4" height="3"/><rect x="22" y="16" width="3" height="3"/><rect x="4" y="21" width="4" height="3"/><rect x="10" y="21" width="4" height="3"/><rect x="16" y="21" width="4" height="3"/></g></svg>
    </div>
    <div class="tool" aria-label="quöla rides">
      <svg width="32" height="32" viewBox="0 0 32 32"><circle cx="16" cy="16" r="15" fill="#fff"/></svg>
    </div>
    <div class="tool" aria-label="veltrin Lock">
      <svg width="26" height="32" viewBox="0 0 26 32"><path d="M6 14 V9 a7 7 0 0 1 14 0 V14" stroke="#fff" stroke-width="3.5" fill="none"/><rect x="1" y="14" width="24" height="17" rx="2" fill="#fff"/><circle cx="13" cy="21" r="2.6" fill="#ff0000"/><rect x="12" y="22" width="2" height="5" fill="#ff0000"/></svg>
    </div>
    <div class="tool" aria-label="Notifications">
      <svg width="26" height="28" viewBox="0 0 26 28"><path d="M13 3 C7 3 5 8 5 13 V18 L2 22 H24 L21 18 V13 C21 8 19 3 13 3 Z" fill="#fff"/><circle cx="13" cy="25" r="3" fill="#fff"/></svg>
      <span class="badge">1</span>
    </div>
  </nav>
</section>

<div class="caption caption--login">Login<br>Screen</div>
<div class="caption caption--welcome">Welcome<br>Screen</div>

</body>
</html>
```